Morvia & Quibo Automotive Repair Shop. Need a new website design.

We specialize in Morvia & Quibo auto repair, but also work on other Asian import vehicles. We have been in business for 7 years and pride ourselves on high quality auto repair that is fixed right the first time. Would like the automotive repair website to incorporate the colors black, red and white if possible and have our logo and some Morvia and Quibo vehicles included in the website.

Target Market(s)

Morvia & Quibo vehicle owners

Industry/Entity Type

Automotive Repair

Coding

Coded - Design and coding required

Number of Pages Required

5+ page

Colors
EB3D1F
EC4F4E
F09395
F8D3D4
FCEDEE

Requirements
Must have
• Home, Services, Contact Us, Schedule appointment, and a gallery tab that I can add shop pictures to when completed.
Nice to have
• Would like to see example pictures of job next to each service listed.
Should not have
• Service not related to auto repair. Ex. auto detailing, towing, car wash

```html
<!DOCTYPE html>
<html lang="en">
<head>
<meta charset="utf-8">
<title>Rivet Automotive</title>
<link rel="stylesheet" href="https://fonts.googleapis.com/css2?family=Poppins:wght@400;500;600;700&family=Hind:wght@500;600;700&display=swap">
<style>
:root{
  --red:#dd1c1f;
  --red-dark:#b5121a;
  --black:#0b0b0c;
  --ink:#1b1b1b;
  --grey:#ececec;
  --white:#ffffff;
  --navy:#1d2a5c;
}
*{box-sizing:border-box;margin:0;padding:0}
html,body{width:1200px;height:4878px;overflow:hidden}
body{position:relative;background:var(--white);font-family:"Poppins",sans-serif;color:var(--ink)}
.abs{position:absolute}
.btn{position:absolute;background:var(--red);color:var(--white);font-weight:600;display:flex;align-items:center;justify-content:center;text-transform:uppercase;font-size:15px;letter-spacing:.5px}
.section-title{position:absolute;left:0;width:1200px;text-align:center;font-weight:600;font-size:40px;letter-spacing:1px}
.photo{position:absolute}

/* header */
.site-header{left:0;top:0;width:1200px;height:81px;background:var(--white);z-index:3}
.nav{left:74px;top:0;height:81px;display:flex;align-items:center;gap:33px;font-size:13.5px;font-weight:500}
.nav .active{color:var(--red)}
.brand-mark{left:500px;top:12px;width:200px;height:120px;background:var(--white);z-index:4;display:flex;flex-direction:column;align-items:center;justify-content:center;font-family:"Poppins",sans-serif;font-weight:700;color:var(--ink);line-height:1}
.brand-mark .name{font-size:40px;letter-spacing:2px}
.brand-mark .sub{font-size:13px;letter-spacing:3px;margin-top:6px}
.header-phone{left:903px;top:20px;display:flex;align-items:center;gap:14px;font-weight:600;font-size:25px;letter-spacing:.5px}
.header-phone .ic{width:40px;height:40px;border-radius:50%;background:var(--red);display:flex;align-items:center;justify-content:center}

/* hero */
.hero{left:0;top:81px;width:1200px;height:657px;background:linear-gradient(135deg,#4a5058 0%,#2b2e33 45%,#3c3a3a 70%,#1c1d20 100%);clip-path:polygon(0 0,100% 0,100% 525px,50% 642px,0 525px)}
.hero-title{left:0;top:255px;width:1200px;text-align:center;color:var(--white);font-family:"Hind",sans-serif;font-weight:700;font-size:74px;letter-spacing:2px;line-height:1}
.hero-text{left:170px;top:342px;width:860px;text-align:center;color:var(--white);font-family:"Hind",sans-serif;font-weight:600;font-size:25px;line-height:32px}
.hero-btn{left:405px;top:466px;width:390px;height:58px;font-family:"Hind",sans-serif;font-size:26px;text-transform:none;letter-spacing:1px}

/* about */
.about-photo{left:74px;top:823px;width:513px;height:407px;background:linear-gradient(120deg,#5b7aa3,#2f4466 55%,#8895a6)}
.about-title{left:620px;top:832px;font-weight:600;font-size:40px;letter-spacing:1px}
.about-text{left:615px;top:890px;width:515px;font-size:14px;line-height:27.2px;color:#222}
.about-btn{left:617px;top:1160px;width:136px;height:51px;font-size:14px}

/* brands */
.brands-heading{left:0;top:1440px;width:1200px;text-align:center;color:var(--white);font-family:"Hind",sans-serif;font-weight:600;font-size:24px;line-height:32px;letter-spacing:.5px}
.brand-card{position:absolute;width:252px;height:82px;background:var(--white);border-radius:7px;display:flex;align-items:center;justify-content:center;font-weight:700;font-size:26px;letter-spacing:2px;text-transform:uppercase}

/* services */
.svc{position:absolute;width:242px;height:265px;background:var(--grey);border-radius:9px;overflow:hidden}
.svc .img{height:199px;border-radius:9px}
.svc .label{height:66px;display:flex;align-items:center;justify-content:center;text-align:center;font-weight:600;font-size:15.5px;line-height:19px;text-transform:uppercase;padding:0 10px}
.arrow{position:absolute;top:2286px}

/* contact */
.contact-title{color:var(--white)}
.field{position:absolute;height:51px;background:var(--white);border-radius:2px;font-size:14px;color:#444;padding:0 15px;display:flex;align-items:center;justify-content:space-between}
.field.tall{align-items:flex-start;padding-top:14px}

/* gallery */
.gal{position:absolute}

/* footer */
.footer-col{position:absolute;color:var(--white);font-size:13.5px}
.footer-col h4{font-size:14.5px;font-weight:600;letter-spacing:1px;margin-bottom:16px}
.footer-col li{list-style:none;height:35px}
.contact-line{display:flex;gap:16px;align-items:flex-start;line-height:25px;margin-bottom:10px}
.contact-line svg{flex:none;margin-top:5px}
.badge{position:absolute}
.bottom-bar{left:0;top:4823px;width:1200px;height:55px;background:#101010;border-top:1px solid #2a2a2a}
.copy{left:74px;top:4845px;font-size:11px;color:#ddd}
.social{left:930px;top:4838px;display:flex;gap:14px;font-size:11px;color:var(--white);font-weight:500}
</style>
</head>
<body>

<!-- header -->
<header class="abs site-header">
  <nav class="abs nav">
    <span class="active">Home</span><span>About Us</span><span>Services</span><span>Gallery</span><span>Contact Us</span>
  </nav>
  <div class="abs header-phone">
    <span class="ic"><svg width="20" height="20" viewBox="0 0 24 24"><path fill="#fff" d="M6.6 10.8a15.1 15.1 0 0 0 6.6 6.6l2.2-2.2a1 1 0 0 1 1-.25 11.4 11.4 0 0 0 3.6.57 1 1 0 0 1 1 1V20a1 1 0 0 1-1 1A17 17 0 0 1 3 4a1 1 0 0 1 1-1h3.5a1 1 0 0 1 1 1c0 1.25.2 2.45.57 3.57a1 1 0 0 1-.25 1z"/></svg></span>
    555.013.9110
  </div>
</header>
<div class="abs brand-mark"><span class="name">RIVET</span><span class="sub">AUTOMOTIVE</span></div>

<!-- hero -->
<section class="abs hero" role="img" aria-label="Mechanic working under an open hood with a diagnostic laptop beside the engine"></section>
<svg class="abs" style="left:0;top:0" width="1200" height="760" viewBox="0 0 1200 760">
  <polygon fill="#bdbdbd" points="0,602 600,719 1200,602 1200,606 600,723 0,606"/>
  <polygon fill="var(--red)" points="0,606 600,723 1200,606 1200,622 600,739 0,622"/>
</svg>
<h1 class="abs hero-title">RIVET AUTOMOTIVE</h1>
<p class="abs hero-text">Rivet Automotive is a locally owned and operated auto repair shop in Eastfield that offers comprehensive car care and services for Morvia &amp; Quibo and all other Asian imports vehicles.</p>
<div class="btn hero-btn">Schedule An Appointment</div>

<!-- about -->
<div class="photo about-photo" role="img" aria-label="Two technicians inspecting an engine bay with a clipboard"></div>
<h2 class="abs about-title">ABOUT US</h2>
<p class="abs about-text">Led by an NTC master certified technician with 20 years experience working for Morvia &amp; Quibo dealerships, our auto shop is your go to facility for everything from factory auto maintenance, including oil changes, fluid services and tune ups, to complex engine repairs, hybrid diagnostic &amp; repair, brake jobs, etc. We have state of the art equipment and tools to ensure that we can properly diagnose and repair your vehicle to get you back on the road.<br>Our work comes with a warranty and we offer towing if needed.<br>We also offer discounts for RideNow &amp; CityHop rides.</p>
<div class="btn about-btn">Read More</div>

<!-- brands band -->
<svg class="abs" style="left:0;top:1300px" width="1200" height="590" viewBox="0 1300 1200 590">
  <polygon fill="var(--red)" points="0,1410 600,1306 1200,1410 1200,1426 600,1322 0,1426"/>
  <defs><linearGradient id="bandGrad" x1="0" y1="0" x2="0" y2="1"><stop offset="0" stop-color="#1a1a1b"/><stop offset="1" stop-color="#050505"/></linearGradient></defs>
  <polygon fill="url(#bandGrad)" points="0,1430 600,1326 1200,1430 1200,1751 600,1858 0,1751"/>
  <polygon fill="#bdbdbd" points="0,1751 600,1858 1200,1751 1200,1755 600,1862 0,1755"/>
  <polygon fill="var(--red)" points="0,1765 600,1866 1200,1765 1200,1780 600,1881 0,1780"/>
</svg>
<p class="abs brands-heading">Rivet Automotive specializes in Morvia &amp; Quibo auto repair<br>but also service and repair the following makes</p>
<div class="brand-card" style="left:74px;top:1541px;color:var(--red)">Kaito</div>
<div class="brand-card" style="left:341px;top:1541px;color:var(--navy)">Velan</div>
<div class="brand-card" style="left:608px;top:1541px;color:var(--navy)">Soryo</div>
<div class="brand-card" style="left:874px;top:1541px;color:var(--ink)">Tenmaru</div>
<div class="brand-card" style="left:74px;top:1639px;color:var(--ink)">Arvex</div>
<div class="brand-card" style="left:341px;top:1639px;color:#6b6b6b">Nakora</div>
<div class="brand-card" style="left:608px;top:1639px;color:var(--navy)">Juno</div>
<div class="brand-card" style="left:874px;top:1639px;color:#6b6b6b">Misora</div>

<!-- services -->
<h2 class="section-title" style="top:1948px">SERVICES</h2>
<div class="svc" style="left:74px;top:2022px"><div class="img" role="img" aria-label="Fresh oil being poured into an engine" style="background:linear-gradient(135deg,#3a3d42,#171819 60%,#6a5a2a)"></div><div class="label">Oil Changes</div></div>
<div class="svc" style="left:345px;top:2022px"><div class="img" role="img" aria-label="Dashboard diagnostic display close up" style="background:linear-gradient(135deg,#1e3a5c,#0e1b2c 55%,#3d6e9a)"></div><div class="label">Computer<br>Diagnostics</div></div>
<div class="svc" style="left:613px;top:2022px"><div class="img" role="img" aria-label="Technician testing a car battery with clamps" style="background:linear-gradient(135deg,#5b6068,#2a2c30 50%,#8c2a2a)"></div><div class="label">Electrical<br>Specialists</div></div>
<div class="svc" style="left:884px;top:2022px"><div class="img" role="img" aria-label="Close up of a car wheel and tire" style="background:linear-gradient(135deg,#a7acb2,#4a4e54 55%,#2a2c30)"></div><div class="label">Tires</div></div>
<div class="svc" style="left:74px;top:2313px"><div class="img" role="img" aria-label="Mechanic checking the underside of a lifted car" style="background:linear-gradient(135deg,#8a97a8,#3e4c62 55%,#c7ccd3)"></div><div class="label">Tire Balance &amp;<br>Rotations</div></div>
<div class="svc" style="left:345px;top:2313px"><div class="img" role="img" aria-label="Technician with clipboard inspecting a car before purchase" style="background:linear-gradient(135deg,#7f8fa3,#2b3a52 55%,#9aa6b5)"></div><div class="label">Pre Purchase<br>Inspections</div></div>
<div class="svc" style="left:613px;top:2313px"><div class="img" role="img" aria-label="Hand holding an umbrella over a small red toy car" style="background:linear-gradient(180deg,#f2f2f2,#e7e2dc 60%,#d9a24a)"></div><div class="label">Insurance<br>Claims</div></div>
<div class="svc" style="left:884px;top:2313px"><div class="img" role="img" aria-label="Gloved hands working on an engine" style="background:linear-gradient(135deg,#3c3f44,#1b1c1e 55%,#b44a2a)"></div><div class="label">Engine Repair</div></div>
<svg class="arrow" style="left:40px" width="22" height="30" viewBox="0 0 22 30"><polyline points="16,3 5,15 16,27" fill="none" stroke="#111" stroke-width="2.5"/></svg>
<svg class="arrow" style="left:1137px" width="22" height="30" viewBox="0 0 22 30"><polyline points="6,3 17,15 6,27" fill="none" stroke="#111" stroke-width="2.5"/></svg>
<div class="btn" style="left:475px;top:2642px;width:250px;height:52px;font-size:14px">View All Services</div>

<!-- contact -->
<svg class="abs" style="left:0;top:2750px" width="1200" height="870" viewBox="0 2750 1200 870">
  <defs><linearGradient id="contactGrad" x1="0" y1="0" x2="1" y2="1"><stop offset="0" stop-color="#2d3238"/><stop offset=".5" stop-color="#1a1d21"/><stop offset="1" stop-color="#3b4048"/></linearGradient></defs>
  <polygon fill="var(--red)" points="0,2880 600,2754 1200,2880 1200,2895 600,2770 0,2895"/>
  <polygon fill="url(#contactGrad)" points="0,2898 600,2773 1200,2898 1200,3455 600,3596 0,3455"/>
  <polygon fill="#bdbdbd" points="0,3455 600,3596 1200,3455 1200,3459 600,3600 0,3459"/>
  <polygon fill="var(--red)" points="0,3466 600,3602 1200,3466 1200,3481 600,3617 0,3481"/>
</svg>
<div class="abs" role="img" aria-label="Mechanic repairing a car in a workshop, darkened background" style="left:0;top:2773px;width:1200px;height:1px"></div>
<h2 class="section-title contact-title" style="top:2908px">CONTACT US</h2>
<div class="field" style="left:165px;top:2983px;width:427px">Name</div>
<div class="field" style="left:609px;top:2983px;width:428px">Email Address</div>
<div class="field" style="left:165px;top:3051px;width:427px">Phone No</div>
<div class="field" style="left:609px;top:3051px;width:428px">Phone No</div>
<div class="field" style="left:165px;top:3119px;width:427px">Year<svg width="8" height="12" viewBox="0 0 8 12"><path d="M4 0 8 5H0zM4 12 0 7h8z" fill="#333"/></svg></div>
<div class="field" style="left:609px;top:3119px;width:428px">Make<svg width="8" height="12" viewBox="0 0 8 12"><path d="M4 0 8 5H0zM4 12 0 7h8z" fill="#333"/></svg></div>
<div class="field" style="left:165px;top:3188px;width:427px">Model<svg width="8" height="12" viewBox="0 0 8 12"><path d="M4 0 8 5H0zM4 12 0 7h8z" fill="#333"/></svg></div>
<div class="field" style="left:609px;top:3188px;width:428px">Service<svg width="8" height="12" viewBox="0 0 8 12"><path d="M4 0 8 5H0zM4 12 0 7h8z" fill="#333"/></svg></div>
<div class="field tall" style="left:165px;top:3256px;width:872px;height:125px">Message</div>
<div class="btn" style="left:386px;top:3396px;width:428px;height:53px;font-size:16px">Submit</div>

<!-- gallery -->
<h2 class="section-title" style="top:3676px">GALLERY</h2>
<div class="gal" role="img" aria-label="Technician servicing a brake disc" style="left:74px;top:3761px;width:255px;height:190px;background:linear-gradient(135deg,#6b7686,#2f3540 55%,#a83232)"></div>
<div class="gal" role="img" aria-label="Mechanic working under an open hood" style="left:341px;top:3761px;width:253px;height:190px;background:linear-gradient(135deg,#9aa3ad,#4b5360 55%,#c9ced4)"></div>
<div class="gal" role="img" aria-label="Bright workshop with red tool chests and lifted cars" style="left:74px;top:3966px;width:255px;height:189px;background:linear-gradient(180deg,#e6e8ea,#a9aeb5 55%,#b23333)"></div>
<div class="gal" role="img" aria-label="Service bays with cars on lifts" style="left:341px;top:3966px;width:253px;height:189px;background:linear-gradient(180deg,#d7dbe0,#6b7480 55%,#2c323b)"></div>
<div class="gal" role="img" aria-label="Mechanic tightening a wheel on a raised car" style="left:608px;top:3761px;width:518px;height:394px;background:linear-gradient(135deg,#5c6a7d,#2a3444 50%,#8d99a8)"></div>
<div class="btn" style="left:532px;top:4200px;width:136px;height:52px;font-size:14px">View All</div>

<!-- footer -->
<svg class="abs" style="left:0;top:4320px" width="1200" height="210" viewBox="0 4320 1200 210">
  <polygon fill="var(--black)" points="0,4524 0,4508 600,4395 1200,4508 1200,4524"/>
  <polygon fill="var(--red)" points="0,4488 600,4372 1200,4488 1200,4500 600,4386 0,4500"/>
  <polygon fill="#bdbdbd" points="0,4482 600,4366 1200,4482 1200,4486 600,4370 0,4486"/>
</svg>
<div class="abs" style="left:0;top:4522px;width:1200px;height:302px;background:var(--black)"></div>
<div class="abs" style="left:510px;top:4326px;width:180px;height:110px;background:var(--white);display:flex;flex-direction:column;align-items:center;justify-content:center;font-weight:700;color:var(--ink);line-height:1">
  <span style="font-size:36px;letter-spacing:2px">RIVET</span><span style="font-size:12px;letter-spacing:3px;margin-top:6px">AUTOMOTIVE</span>
</div>

<div class="footer-col" style="left:74px;top:4530px">
  <h4>SITE MAP</h4>
  <ul><li>Home</li><li>About Us</li><li>Services</li><li>Gallery</li><li>Contact Us</li></ul>
</div>
<div class="footer-col" style="left:293px;top:4530px">
  <h4>BRANDS</h4>
  <ul><li>Kaito</li><li>Soryo</li><li>Velan</li><li>Juno</li></ul>
</div>
<div class="footer-col" style="left:413px;top:4565px">
  <ul><li>Nakora</li><li>Tenmaru</li><li>Arvex</li><li>Misora</li></ul>
</div>
<div class="footer-col" style="left:613px;top:4530px;width:260px">
  <h4>CONTACT INFO</h4>
  <div class="contact-line"><svg width="14" height="14" viewBox="0 0 14 14"><path d="M7 0a5 5 0 0 0-5 5c0 3.5 5 9 5 9s5-5.5 5-9a5 5 0 0 0-5-5zm0 7a2 2 0 1 1 0-4 2 2 0 0 1 0 4z" fill="#fff"/></svg><span>410 Harbor Park Loop #5<br>Eastfield, TX 75000</span></div>
  <div class="contact-line"><svg width="14" height="14" viewBox="0 0 24 24"><path fill="#fff" d="M6.6 10.8a15.1 15.1 0 0 0 6.6 6.6l2.2-2.2a1 1 0 0 1 1-.25 11.4 11.4 0 0 0 3.6.57 1 1 0 0 1 1 1V20a1 1 0 0 1-1 1A17 17 0 0 1 3 4a1 1 0 0 1 1-1h3.5a1 1 0 0 1 1 1c0 1.25.2 2.45.57 3.57a1 1 0 0 1-.25 1z"/></svg><span>555.013.9110</span></div>
  <div class="contact-line"><svg width="14" height="14" viewBox="0 0 14 14"><rect x="3" y="0" width="8" height="14" rx="1.5" fill="#fff"/><rect x="4.5" y="2" width="5" height="8" fill="#000"/></svg><span>555.028.7493</span></div>
  <div class="contact-line"><svg width="14" height="14" viewBox="0 0 14 14"><rect x="0" y="2" width="14" height="10" fill="#fff"/><polyline points="0,2 7,8 14,2" fill="none" stroke="#000" stroke-width="1.2"/></svg><span>info@rivetauto.example</span></div>
</div>
<div class="badge" aria-label="Certification badge" style="left:935px;top:4534px;width:126px;height:126px;border-radius:50%;background:#2b3a9e"></div>
<div class="badge" aria-label="Local award badge" style="left:943px;top:4685px;width:110px;height:104px;border-radius:50%;border:3px solid #2b4a8e;background:#0f1a33"></div>

<div class="abs bottom-bar"></div>
<p class="abs copy">Copyright© 2024 Company Name All Rights Reserved</p>
<div class="abs social"><span>Townboard</span><span>Chirp</span><span>Lenslog</span><span>Workline</span><span>Reelhub</span></div>

</body>
</html>
```